Design a newsletter for a crypto gateway payment company

The project is about making the design for a newsletter (sent by email) for a crypto payment gateway. The design should include all usual and necessary parts found in a newsletter (header, one main article with illustration and link to the full content, some secondary articles with or without illustration and link to the company blog, footer with links to unsubscribe page and various information about the company, section separator, secondary articles ...).
The design may re-use some elements from the company web site https://quorvelpay.io, but feel free to innovate.
The design should be responsive and be as good in all email clients and all sizes of display from handset to desktop with everything in between.
I've added a few screenshot of the previous newsletter as they were sent to users.
Good luck and be an artist. No AI stuff, please.

```html
<!DOCTYPE html>
<html lang="en">
<head>
<meta charset="UTF-8">
<title>Digital Currencies for Daily Transactions – Newsletter</title>
<link rel="stylesheet" href="https://fonts.googleapis.com/css2?family=Poppins:wght@400;500;600;700&display=swap">
<style>
  :root {
    --sky-top: #b1ecec;
    --sky-mid: #a6cfee;
    --sky-low: #8d9fe0;
    --page-bg: #adbdee;
    --panel-bg: #c6d2fb;
    --card-top: #7289d6;
    --card-bottom: #99ade3;
    --band-bg: #9caee0;
    --headline: #7f93dc;
    --nav-text: #5a62a8;
    --orange: #f5921e;
    --yellow: #fff200;
    --white: #ffffff;
    --partner-green: #22e022;
    --icon-ink: #4a4f6a;
    --muted: #6f7488;
  }
  * { box-sizing: border-box; margin: 0; padding: 0; }
  html, body { width: 1200px; height: 3561px; overflow: hidden; }
  body {
    position: relative;
    background: var(--page-bg);
    font-family: "Poppins", sans-serif;
    color: var(--white);
  }
  .abs { position: absolute; }
  .hero-bg { left: 0; top: 0; width: 1200px; height: 1420px; }
  .nav { top: 84px; left: 0; width: 1200px; height: 28px; }
  .nav a {
    position: absolute; top: 0; font-size: 18px; font-weight: 500;
    color: var(--nav-text); text-decoration: none; letter-spacing: 1px;
    transform: translateX(-50%); white-space: nowrap;
  }
  .headline {
    top: 192px; left: 0; width: 1200px; text-align: center;
    font-size: 52px; font-weight: 700; line-height: 68px;
    color: var(--headline); letter-spacing: -0.5px;
  }
  .btn {
    display: flex; align-items: center; justify-content: center;
    background: var(--orange); color: var(--white); text-decoration: none;
    font-weight: 600; border-radius: 40px; white-space: nowrap;
  }
  .btn-contact { left: 434px; top: 368px; width: 340px; height: 57px; font-size: 23px; letter-spacing: 0.5px; }
  .hero-art {
    left: 75px; top: 495px; width: 1030px; height: 745px; border-radius: 50% 50% 46% 46%;
    background: radial-gradient(ellipse at 55% 45%, #e6f2ff 0%, #a9c4f2 40%, #7d93de 75%, rgba(141,159,224,0) 100%);
  }
  .panel { left: 126px; top: 1526px; width: 947px; height: 614px; background: var(--panel-bg); border-radius: 44px; }
  .card { top: 1566px; width: 403px; height: 439px; border-radius: 28px; overflow: hidden; background: var(--card-bottom); }
  .card-1 { left: 172px; }
  .card-2 { left: 620px; }
  .card-head {
    position: absolute; left: 0; top: 0; width: 100%; height: 264px; background: var(--card-top);
    display: flex; flex-direction: column; justify-content: center; align-items: center;
    text-align: center; font-weight: 600; font-size: 20px; line-height: 35px; text-transform: uppercase;
  }
  .card-head .hl { color: var(--yellow); font-weight: 700; font-size: 25px; }
  .card-notch { position: absolute; top: 263px; left: 161px; }
  .card-body {
    position: absolute; left: 30px; right: 30px; top: 300px; bottom: 20px;
    display: flex; align-items: center; justify-content: center; text-align: center;
    font-size: 19px; line-height: 27px; font-weight: 400;
  }
  .btn-learn { top: 2041px; width: 243px; height: 62px; font-size: 22px; }
  .band { left: 0; top: 2274px; width: 1200px; height: 416px; background: var(--band-bg); }
  .partner-name {
    top: 2318px; left: 0; width: 1200px; text-align: center;
    font-size: 84px; font-weight: 600; color: var(--partner-green); line-height: 100px;
  }
  .partner-stats {
    top: 2436px; left: 0; width: 1200px; text-align: center;
    font-size: 28px; font-weight: 600; line-height: 37px;
  }
  .btn-partner { left: 262px; top: 2545px; width: 674px; height: 94px; font-size: 32px; border-radius: 50px; }
  .divider { left: 0; top: 2684px; }
  .about-title { top: 2822px; left: 0; width: 1200px; text-align: center; font-size: 53px; font-weight: 500; letter-spacing: 2px; }
  .about-text {
    top: 2914px; left: 170px; width: 860px; text-align: center;
    font-size: 18px; line-height: 30.5px; font-weight: 400;
  }
  .btn-about { left: 476px; top: 3152px; width: 243px; height: 62px; font-size: 22px; }
  .social { left: 0; top: 3313px; width: 1200px; height: 80px; }
  .copyright { top: 3432px; left: 0; width: 1200px; text-align: center; font-size: 21px; color: var(--muted); }
</style>
</head>
<body>

  <svg class="abs hero-bg" viewBox="0 0 1200 1420" aria-hidden="true">
    <defs>
      <linearGradient id="skyFade" x1="0" y1="0" x2="0" y2="1">
        <stop offset="0" stop-color="#b1ecec"/>
        <stop offset="0.35" stop-color="#a6d6ef"/>
        <stop offset="0.7" stop-color="#93ade4"/>
        <stop offset="1" stop-color="#8a9bdf"/>
      </linearGradient>
    </defs>
    <path d="M0 0 H1200 V1260 Q600 1520 0 1260 Z" fill="url(#skyFade)"/>
    <path d="M0 1260 Q600 1520 1200 1260 V1280 Q600 1440 0 1280 Z" fill="#8696da" opacity="0.6"/>
  </svg>

  <nav class="abs nav">
    <a href="#" style="left:405px">Home</a>
    <a href="#" style="left:510px">Service</a>
    <a href="#" style="left:636px">Contact Us</a>
    <a href="#" style="left:777px">About Us</a>
  </nav>

  <h1 class="abs headline">DIGITAL CURRENCIES FOR<br>DAILY TRANSACTIONS</h1>

  <a class="abs btn btn-contact" href="https://quorvelpay.io">CONTACT US</a>

  <div class="abs hero-art" role="img" aria-label="Illustration of a globe and smartphone surrounded by crypto coins, a security padlock, an airplane and a shopping cart"></div>

  <div class="abs panel"></div>

  <article class="abs card card-1">
    <div class="card-head">
      <span>Why is the</span>
      <span class="hl">$1.2 Trillion<br>Freelance Economy</span>
      <span>Embracing digiral<br>currency payments ?</span>
    </div>
    <svg class="card-notch" width="82" height="34" viewBox="0 0 82 34" aria-hidden="true"><path d="M0 0 H82 L41 34 Z" fill="#7289d6"/></svg>
    <p class="card-body">Why Digital Currency Payments are so Prevalent withn the gig economy ?.</p>
  </article>

  <article class="abs card card-2">
    <div class="card-head">
      <span>Learn how the</span>
      <span class="hl">$8.6Trillion<br>Travel Industry</span>
      <span>has changed in the<br>post-pandemic boom ?</span>
    </div>
    <svg class="card-notch" width="82" height="34" viewBox="0 0 82 34" aria-hidden="true"><path d="M0 0 H82 L41 34 Z" fill="#7289d6"/></svg>
    <p class="card-body">Why Tourism businesses staying ahed in this competitive landscape with digital currency payments ?.</p>
  </article>

  <a class="abs btn btn-learn" style="left:253px" href="https://quorvelpay.io">Learn More</a>
  <a class="abs btn btn-learn" style="left:701px" href="https://quorvelpay.io">Learn More</a>

  <section class="abs band"></section>
  <div class="abs partner-name">Rydelo</div>
  <p class="abs partner-stats">37.7 million monthly &nbsp;|&nbsp; transacting users and<br>5 million merchant-partners</p>
  <a class="abs btn btn-partner" href="https://quorvelpay.io">Read more about our Partnership</a>

  <svg class="abs divider" width="1200" height="70" viewBox="0 0 1200 70" aria-hidden="true">
    <path d="M0 6 H560 L596 62 L632 6 H1200" fill="none" stroke="#f5921e" stroke-width="9"/>
  </svg>

  <h2 class="abs about-title">About Us</h2>
  <p class="abs about-text">Lorem ipsum dolor sit amet, consectetur adipiscing elit, sed do eiusmod tempor incididunt ut labore et dolore magna aliqua. Ut enim ad minim veniam, quis nostrud exercitation ullamco laboris nisi ut aliquip ex ea commodo consequat. Duis aute irure dolor in reprehenderit in voluptate velit esse cillum dolore eu fugiat nulla pariatur. Excepteur sint occaecat cupidatat non proident, sunt in culpa qui officia deserunt mollit anim id est laborum.</p>

  <a class="abs btn btn-about" href="https://quorvelpay.io">Learn More</a>

  <svg class="abs social" viewBox="0 0 1200 80" aria-label="Social media links">
    <g fill="none" stroke="#4a4f6a" stroke-width="3">
      <circle cx="391" cy="40" r="37"/>
      <circle cx="496" cy="40" r="37"/>
      <circle cx="598" cy="40" r="37"/>
      <circle cx="703" cy="40" r="37"/>
      <circle cx="805" cy="40" r="37"/>
    </g>
  </svg>

  <p class="abs copyright">Copyright@mycompany 2024. All right reserved</p>

</body>
</html>
```